Kowalczyk Electric & Sons

We need a logo design and business card design for our electrical company. I would like to see designs with lightning and the bright green lettering.

Target Market(s)

Electrical contractor

Industry/Entity Type

Business

Contact Information for Business Card

204-558-WIRE(9473)
Marty Kowalczyk
www.kowalczykelectric.example
Owner

Colors
acd136

Requirements
Must have
• - New Construction
• - Commercial
• - Residential
• - Tenant improvements
• - Preventative Maintenance
• - Re-Models
• - Service Upgrades
• - Trouble Shooting
• - New Circuits
• All your electrical needs
• Lighting up Winnipeg and surrounding areas !

```html
<!DOCTYPE html>
<html lang="en">
<head>
<meta charset="utf-8">
<title>Kowalczyk Electric &amp; Sons – Business Card</title>
<link href="https://fonts.googleapis.com/css2?family=Rajdhani:wght@500;600;700&display=swap" rel="stylesheet">
<style>
  :root {
    --stage: #1a1a1a;
    --card: #000000;
    --green: #acd136;
    --violet: #8a4dff;
    --violet-deep: #3a1670;
    --glow: #f4e9ff;
    --bullet: #d8d8d8;
  }
  * { box-sizing: border-box; margin: 0; padding: 0; }
  html, body {
    width: 1200px; height: 800px; overflow: hidden;
    background: var(--stage);
    font-family: "Rajdhani", sans-serif;
  }
  .sheet {
    position: relative; width: 1200px; height: 800px;
    display: flex; align-items: center; justify-content: center; gap: 50px;
  }
  .card {
    position: relative; width: 540px; height: 309px;
    background: var(--card); overflow: hidden;
    box-shadow: 0 18px 40px rgba(0,0,0,.6);
  }
  .lightning { position: absolute; }

  /* front */
  .front .lightning {
    right: -40px; top: 20px; width: 440px; height: 300px;
    background: radial-gradient(ellipse at 90% 50%, var(--glow) 0%, var(--violet) 12%, var(--violet-deep) 38%, rgba(0,0,0,0) 70%);
  }
  .front .brand {
    position: absolute; left: 30px; top: 30px;
    color: var(--green); font-weight: 700; font-size: 34px;
    line-height: 1; letter-spacing: 1px; text-transform: uppercase;
  }
  .front .brand span { display: block; font-size: 20px; margin-top: 4px; letter-spacing: 2px; }
  .contact { position: absolute; left: 30px; top: 122px; color: var(--green); }
  .contact .name { font-weight: 700; font-size: 22px; text-transform: uppercase; }
  .contact .role { font-weight: 500; font-size: 15px; margin-bottom: 8px; }
  .contact p { font-weight: 500; font-size: 16px; line-height: 1.3; }
  .contact .tagline { margin-top: 6px; }

  /* back */
  .back .lightning.top {
    left: 140px; top: -60px; width: 320px; height: 200px;
    background: radial-gradient(ellipse at 50% 0%, var(--violet) 0%, var(--violet-deep) 40%, rgba(0,0,0,0) 72%);
  }
  .back .lightning.bottom {
    right: -30px; bottom: -70px; width: 360px; height: 220px;
    background: radial-gradient(ellipse at 60% 100%, var(--glow) 0%, var(--violet) 18%, var(--violet-deep) 45%, rgba(0,0,0,0) 75%);
  }
  .services {
    position: absolute; left: 34px; top: 34px; list-style: none;
    color: var(--green); font-weight: 600; font-size: 16px; line-height: 1.28;
  }
  .services li { display: flex; align-items: center; gap: 8px; }
  .services li::before {
    content: ""; width: 8px; height: 8px; border-radius: 50%;
    border: 1.5px solid var(--bullet); flex: none;
  }
  .back .brand {
    position: absolute; right: 28px; top: 118px; text-align: right;
    color: var(--green); font-weight: 700; font-size: 30px;
    line-height: 1; letter-spacing: 1px; text-transform: uppercase;
  }
  .back .brand span { display: block; font-size: 18px; margin-top: 4px; letter-spacing: 2px; }
</style>
</head>
<body>
<main class="sheet">
  <section class="card front">
    <div class="lightning" role="img" aria-label="Purple lightning bolts bursting from the right edge"></div>
    <h1 class="brand">Kowalczyk <span>Electric &amp; Sons</span></h1>
    <div class="contact">
      <h2 class="name">Marty Kowalczyk</h2>
      <div class="role">Owner</div>
      <p>204-558-WIRE(9473)</p>
      <p>mkowalczyk@mailbox.example</p>
      <p>www.kowalczykelectric.example</p>
      <p class="tagline">Lighting up Winnipeg and surrounding areas !</p>
    </div>
  </section>

  <section class="card back">
    <div class="lightning top" role="img" aria-label="Purple lightning bolts along the top edge"></div>
    <div class="lightning bottom" role="img" aria-label="Purple lightning bolts rising from the bottom corner"></div>
    <ul class="services">
      <li>New Construction</li>
      <li>Commercial</li>
      <li>Residential</li>
      <li>Tenant Improvements</li>
      <li>Preventative Maintenance</li>
      <li>Re-Models</li>
      <li>Service Upgrades</li>
      <li>Trouble Shooting</li>
      <li>New Circuits</li>
      <li>All your electrical needs</li>
    </ul>
    <div class="brand">Kowalczyk <span>Electric &amp; Sons</span></div>
  </section>
</main>
</body>
</html>
```